依頼概要
■依頼の目的/概要
薬局で作っているかぜ薬の販促用のポスターを作成して頂きたいです。

■依頼詳細
以下の4つの文言と当社の社長の写真を入れたポスターのデザインをお願いします。

・私が毎日心を込めて作っております(キャッチコピー)
・薬剤師手作りのかぜ薬(キャッチコピーの下に一回り小さい文字でいれる)
・一度飲んだら手放せなくなります
・特に仕事で忙しくて病院に行けない方はご家庭に必携です
・社長の写真

薬局内に掲示するポスターになります。
実際に掲示するポスターのサイズはA0サイズで考えていますが、デザインはA4サイズでの作成をお願いいたします。
※社長の写真は添付ファイルにてご確認ください。

その他何かご不明な点がございましたら、お気軽にご質問下さい。
よろしくお願いいたします。
ポスター内の文字に関して、縦書きなら縦書き、横書きなら横書きに統一をお願いいたします。

仕事で忙しい方にも目にとまるようなデザインだったので、選ばせていただきました。

提案していただいたランサーの皆さん、ありがとうございました。

```html
<!DOCTYPE html>
<html lang="ja">
<head>
<meta charset="utf-8">
<title>薬剤師手作りのかぜ薬</title>
<link rel="stylesheet" href="https://fonts.googleapis.com/css2?family=Yuji+Syuku&family=Shippori+Mincho:wght@500;700&family=Noto+Sans+JP:wght@500;700&display=swap">
<style>
  :root {
    --navy: #1c2f6e;
    --sky: #dfe8f6;
    --ink: #1a1a1a;
    --red: #d4123a;
    --rose: #f9e4ea;
    --rose-deep: #c8234d;
    --paper: #ffffff;
  }
  * { margin: 0; padding: 0; box-sizing: border-box; }
  html, body { width: 849px; height: 1200px; overflow: hidden; background: var(--paper); }
  .poster {
    position: relative; width: 849px; height: 1200px; overflow: hidden;
    background: linear-gradient(180deg, var(--paper) 0%, var(--paper) 75%, var(--sky) 100%);
    border: 14px solid var(--sky);
  }
  .shop-name {
    position: absolute; top: 14px; right: 26px;
    font: 500 22px "Noto Sans JP", sans-serif; color: var(--navy);
  }
  .portrait {
    position: absolute; left: 70px; top: 70px; width: 510px; height: 312px;
    background: linear-gradient(135deg, #eef1f4 0%, #c9cfd6 45%, #8c96a3 100%);
  }
  .portrait-caption {
    position: absolute; left: 410px; top: 322px;
    font: 500 15px/1.35 "Noto Sans JP", sans-serif; color: var(--ink);
  }
  .headline { font: 400 70px/1 "Yuji Syuku", serif; color: var(--ink); }
  .headline-line {
    position: absolute; writing-mode: vertical-rl; display: block; width: 72px;
  }
  .headline-line.first { left: 712px; top: 105px; letter-spacing: 2px; }
  .headline-line.second { left: 592px; top: 200px; letter-spacing: 34px; }
  .headline .heart { color: var(--red); }
  .point {
    position: absolute; top: 410px; width: 40px; writing-mode: vertical-rl;
    font: 700 32px/40px "Shippori Mincho", serif; color: var(--ink);
  }
  .point .dot { color: var(--red); }
  .point.one { left: 532px; }
  .point.two { left: 470px; }
  .point.three { left: 408px; top: 442px; }
  .product-tag {
    position: absolute; left: 70px; top: 396px; width: 156px; height: 552px;
    background: var(--rose); border-radius: 10px;
    writing-mode: vertical-rl; padding-top: 34px;
    font: 400 58px/156px "Yuji Syuku", serif; color: var(--rose-deep);
  }
  .product-name {
    position: absolute; left: 240px; top: 880px; width: 120px; height: 236px;
    background: var(--navy); border-radius: 10px;
    writing-mode: vertical-rl; display: flex; align-items: center; justify-content: center;
    font: 400 64px/1 "Yuji Syuku", serif; color: var(--paper);
  }
  .footer-band {
    position: absolute; left: -14px; right: -14px; bottom: -14px; height: 72px;
    background: var(--navy); display: flex; align-items: center; justify-content: center;
    font: 700 21px "Noto Sans JP", sans-serif; color: var(--paper); letter-spacing: 1px;
  }
</style>
</head>
<body>
<div class="poster">
  <p class="shop-name">○○薬局</p>
  <div class="portrait" role="img" aria-label="調剤する薬局代表の写真"></div>
  <p class="portrait-caption">○○薬局 代表<br>○○ 太郎</p>

  <h1 class="headline">
    <span class="headline-line first">私が毎日<span class="heart">心</span>を込めて</span>
    <span class="headline-line second">作っております。</span>
  </h1>

  <p class="point one"><span class="dot">●</span>一度飲んだら手放せなくなります。</p>
  <p class="point two"><span class="dot">●</span>特に仕事で忙しくて病院に</p>
  <p class="point three">行けない方はご家庭に必携です。</p>

  <p class="product-tag">薬剤師手作りの</p>
  <p class="product-name">かぜ薬</p>

  <p class="footer-band">お求めはお気軽にスタッフまでお申し付けください。</p>
</div>
</body>
</html>
```